Corkmill Cafe' eLiquid Label - retro, trendy design

Need a 1.5"x3" label designed for an eLiquid bottle. I like the distressed retro diner look. Feel free to take creative license on logo, images etc. Attaching a mockup I did just to give you an idea of what look I want - the attached concept has all textual elements required....want retro trendy....hollowell-ish look and personality...warm colors...high contrasts. attached Vesk image is the mockup I want redesigned.

Target Market(s)

eclectic

Industry/Entity Type

Cafe

Font styles to use
Serif
Decorative

Requirements
Must have
• text elements from uploaded sample - 1.5x3 inch high res
Nice to have
• incorporate QN logo somewhere in the design - attached

```html
<!DOCTYPE html>
<html lang="en">
<head>
<meta charset="utf-8">
<title>Corkmill Vapor – Tiramisu label options</title>
<link rel="stylesheet" href="https://fonts.googleapis.com/css2?family=Cinzel:wght@500;600;700&family=Open+Sans:wght@600;700&display=swap">
<style>
  :root {
    --backdrop: #f1f1f1;
    --label-black: #121212;
    --damask: #1e1e1e;
    --gold: #d9b25a;
    --gold-deep: #a87b2c;
    --cream: #f4e8c6;
    --cream-edge: #e3cd93;
    --ink: #111111;
    --white: #ffffff;
    --tag-pink: #fb8cfb;
    --tag-magenta: #e81ee8;
    --bottle-brown: #2a1a12;
  }
  * { box-sizing: border-box; margin: 0; padding: 0; }
  html, body { width: 1200px; height: 1137px; overflow: hidden; }
  body {
    position: relative;
    background: var(--backdrop);
    font-family: "Open Sans", Arial, sans-serif;
  }

  .option-number {
    position: absolute;
    top: 51px;
    width: 108px; height: 108px;
    border-radius: 50%;
    background: var(--white);
    color: var(--tag-magenta);
    font: 700 60px/108px "Open Sans", Arial, sans-serif;
    text-align: center;
  }
  .option-number--one { left: 278px; }
  .option-number--two { left: 790px; }

  .revision-tag {
    position: absolute;
    left: 353px; top: 182px;
    width: 477px; height: 91px;
    background: var(--tag-pink);
    border: 2px solid var(--ink);
    text-align: center;
    color: var(--ink);
  }
  .revision-tag__title { font: 700 30px/1 "Open Sans", Arial, sans-serif; margin-top: 14px; }
  .revision-tag__date { font: 700 20px/1 "Open Sans", Arial, sans-serif; margin-top: 10px; }

  .label {
    position: absolute;
    top: 487px;
    width: 420px; height: 491px;
    background: var(--label-black);
    border-top: 5px solid var(--gold);
    overflow: hidden;
    text-align: center;
  }
  .label--one { left: 127px; }
  .label--two { left: 634px; }

  .label__pattern {
    position: absolute; inset: 0;
    background: radial-gradient(circle at 50% 45%, var(--damask), var(--label-black) 75%);
  }

  .label__brand {
    position: absolute; left: 0; right: 0; top: 48px;
    font: 700 34px/1 "Cinzel", serif;
    color: var(--gold);
    letter-spacing: 1px;
  }
  .label__tagline {
    position: absolute; left: 0; right: 0; top: 91px;
    font: 600 16px/1 "Open Sans", Arial, sans-serif;
    color: var(--white);
    letter-spacing: 0.3px;
  }

  .label__ornament {
    position: absolute; top: 200px;
    width: 140px; height: 56px;
  }
  .label__ornament--left {
    left: 0;
    background: linear-gradient(90deg, rgba(168,123,44,0.1), rgba(217,178,90,0.55));
  }
  .label__ornament--right {
    right: 0;
    background: linear-gradient(270deg, rgba(168,123,44,0.1), rgba(217,178,90,0.55));
  }

  .label__mark {
    position: absolute; left: 140px; top: 174px;
    width: 140px; height: 110px;
    display: flex; align-items: center; justify-content: center; gap: 10px;
  }
  .label__mark-dot { width: 16px; height: 16px; border-radius: 50%; }
  .label__mark-name { font: 700 48px/1 "Cinzel", serif; }
  .label--one .label__mark-dot { background: var(--white); }
  .label--one .label__mark-name { color: var(--white); }
  .label--two .label__mark-dot { background: var(--gold); }
  .label--two .label__mark-name { color: var(--gold); }

  .label__flavour {
    position: absolute; left: 0; right: 0; top: 298px;
    font: 600 56px/1 "Cinzel", serif;
    color: var(--white);
    letter-spacing: 5px;
  }
  .label__rule {
    position: absolute; left: 18px; right: 18px; top: 360px;
    height: 2px; background: var(--white); opacity: 0.85;
  }
  .label__strength {
    position: absolute; left: 0; right: 0; top: 392px;
    font: 600 17px/1 "Open Sans", Arial, sans-serif;
    color: var(--white);
  }
  .label__specs {
    position: absolute; left: 0; right: 0; top: 423px;
    height: 52px;
    background: linear-gradient(180deg, var(--cream-edge), var(--cream) 25%, var(--cream) 75%, var(--cream-edge));
    font: 600 21px/52px "Open Sans", Arial, sans-serif;
    color: var(--ink);
  }
  .label__specs-star { color: var(--gold-deep); font-size: 17px; margin: 0 6px; }
  .label__foot {
    position: absolute; left: 0; right: 0; top: 475px; bottom: 0;
    background: var(--bottle-brown);
  }
</style>
</head>
<body>
  <div class="option-number option-number--one">1</div>
  <div class="option-number option-number--two">2</div>

  <div class="revision-tag">
    <p class="revision-tag__title">REVISED DESIGN</p>
    <p class="revision-tag__date">FEB.5.2016</p>
  </div>

  <section class="label label--one">
    <div class="label__pattern" role="img" aria-label="Dark damask wallpaper pattern"></div>
    <h1 class="label__brand">CORKMILL VAPOR</h1>
    <p class="label__tagline">ULTRA-PREMIUM MOD GREASE</p>
    <div class="label__ornament label__ornament--left" role="img" aria-label="Gold scroll ornament"></div>
    <div class="label__ornament label__ornament--right" role="img" aria-label="Gold scroll ornament"></div>
    <div class="label__mark"><span class="label__mark-dot"></span><span class="label__mark-name">QN</span></div>
    <h2 class="label__flavour">TIRAMISU</h2>
    <div class="label__rule"></div>
    <p class="label__strength">12 mg Nicotine</p>
    <p class="label__specs">30 ml<span class="label__specs-star">★</span>70/30</p>
    <div class="label__foot"></div>
  </section>

  <section class="label label--two">
    <div class="label__pattern" role="img" aria-label="Dark damask wallpaper pattern"></div>
    <h1 class="label__brand">CORKMILL VAPOR</h1>
    <p class="label__tagline">ULTRA-PREMIUM MOD GREASE</p>
    <div class="label__ornament label__ornament--left" role="img" aria-label="Gold scroll ornament"></div>
    <div class="label__ornament label__ornament--right" role="img" aria-label="Gold scroll ornament"></div>
    <div class="label__mark"><span class="label__mark-dot"></span><span class="label__mark-name">QN</span></div>
    <h2 class="label__flavour">TIRAMISU</h2>
    <div class="label__rule"></div>
    <p class="label__strength">12 mg Nicotine</p>
    <p class="label__specs">30 ml<span class="label__specs-star">★</span>70/30</p>
    <div class="label__foot"></div>
  </section>
</body>
</html>
```